corwin's pastel

We are a family business based in sydney introducing a common brazilian street food into sydney cafes and restaurants.
what we provide are pastels which is a thinly crust pie with assorted fillings
we mainly focus on supplying cafes and restaurants but we do sell privately.
We have had a few cafes ask to stock our cards due to customer request. except we don't have any!! hence why we need you. : )
I have attached an image of our pastels which is just to give you an idea of what they look like.
Updates
I have just seen all the designs and am impressed by some of your work. I will have to sit with my parter later today and will hopefully have some more constructive feedback and a decision soon.
Hello designers,
Hello designers,
Target Market(s)
cafe's and restaurants
Industry/Entity Type
Business
Contact Information for Business Card
Corwin's pastel
joaquim 0468217094
corwinspastel@fernmail.example

```html
<!DOCTYPE html>
<html lang="en">
<head>
<meta charset="utf-8">
<title>Corwin's pastel – business card</title>
<link rel="stylesheet" href="https://fonts.googleapis.com/css2?family=Arimo:wght@400&display=swap">
<style>
  :root {
    --page: #ffffff;
    --card: #000000;
    --card-shadow: #555555;
    --guide: #b5b5b5;
    --wave: #4d4d4d;
    --text: #a9a9a9;
    --icon: #ffffff;
  }
  html, body {
    margin: 0;
    padding: 0;
    width: 1200px;
    height: 1000px;
    overflow: hidden;
    background: var(--page);
  }
  .canvas {
    position: relative;
    width: 1200px;
    height: 1000px;
    font-family: "Arimo", Arial, sans-serif;
  }
  .card-guide {
    position: absolute;
    left: 297px;
    top: 140px;
    width: 681px;
    height: 392px;
    border: 1px dotted var(--guide);
    box-sizing: border-box;
  }
  .card {
    position: absolute;
    left: 299px;
    top: 142px;
    width: 674px;
    height: 385px;
    background: var(--card);
    box-shadow: 6px 6px 0 var(--card-shadow);
    overflow: hidden;
  }
  .card__wave {
    position: absolute;
    left: 0;
    top: 0;
  }
  .card__name {
    position: absolute;
    left: 121px;
    top: 72px;
    margin: 0;
    font-size: 46px;
    font-weight: 400;
    color: var(--text);
    white-space: nowrap;
  }
  .contact {
    position: absolute;
    left: 40px;
    top: 275px;
    margin: 0;
    padding: 0;
    list-style: none;
  }
  .contact__item {
    display: flex;
    align-items: center;
    height: 37px;
    font-size: 29px;
    color: var(--text);
    white-space: nowrap;
  }
  .contact__icon {
    width: 34px;
    height: 30px;
    margin-right: 12px;
    flex: none;
  }
</style>
</head>
<body>
<div class="canvas">
  <div class="card-guide"></div>
  <section class="card" aria-label="Corwin's pastel business card">
    <svg class="card__wave" width="674" height="385" viewBox="0 0 674 385" aria-hidden="true">
      <path fill="var(--wave)" d="M0,178 C60,155 130,148 200,170 C300,200 420,268 540,276 C600,280 640,262 674,250 L674,290 C640,300 600,306 555,305 C430,300 300,225 205,216 C140,210 60,215 0,233 Z"/>
    </svg>
    <h1 class="card__name">Corwin's pastel joaquim</h1>
    <ul class="contact">
      <li class="contact__item">
        <svg class="contact__icon" viewBox="0 0 34 30" aria-hidden="true">
          <path fill="var(--icon)" d="M17,1 h6 v8 h-4 c-2,3 -2,9 0,12 h4 v8 h-6 c-6,-5 -6,-23 0,-28 Z"/>
          <rect x="24" y="1" width="4" height="8" fill="var(--icon)"/>
          <rect x="24" y="21" width="4" height="8" fill="var(--icon)"/>
        </svg>
        <span>0468217094</span>
      </li>
      <li class="contact__item">
        <svg class="contact__icon" viewBox="0 0 34 30" aria-hidden="true">
          <rect x="1" y="5" width="32" height="21" fill="var(--icon)"/>
          <path d="M1,5 L17,18 L33,5 M1,26 L13,15 M33,26 L21,15" stroke="var(--card)" stroke-width="1.8" fill="none"/>
        </svg>
        <span>corwinspastel@fernmail.example</span>
      </li>
    </ul>
  </section>
</div>
</body>
</html>
```